Realty Group Needs Classy, Contemporary Letterhead Design

We need a letterhead design for a new realty company located in NY, USA. We buy investment properties to rehabilitate and or keep in our rental portfolio.

```html
<!DOCTYPE html>
<html lang="en">
<head>
<meta charset="utf-8">
<title>Meridian Realty Group – Letterhead</title>
<link href="https://fonts.googleapis.com/css2?family=Open+Sans:wght@400;600;800&family=Lato:wght@400&display=swap" rel="stylesheet">
<style>
  :root {
    --brand-purple: #4f2a87;
    --brand-purple-soft: #7a59b0;
    --ink: #3d3d3d;
    --ink-soft: #555555;
    --paper: #ffffff;
    --backdrop: #e4e4e4;
    --rule: #6b6b6b;
  }
  * { margin: 0; padding: 0; box-sizing: border-box; }
  html, body {
    width: 1040px; height: 1200px; overflow: hidden;
    background: var(--backdrop);
    font-family: "Open Sans", Arial, sans-serif;
  }
  .letterhead {
    position: absolute; left: 60px; top: 10px;
    width: 920px; height: 1180px;
    background: var(--paper);
    box-shadow: 0 2px 10px rgba(0,0,0,0.18);
  }
  .brand {
    position: absolute; top: 50px; left: 0; width: 100%;
    text-align: center;
  }
  .brand-name {
    font-family: "Open Sans", Arial, sans-serif;
    font-weight: 800; font-size: 42px; letter-spacing: -1px;
    color: var(--brand-purple); line-height: 1;
  }
  .brand-tagline {
    display: flex; align-items: center; justify-content: center; gap: 8px;
    margin-top: 2px;
    font-size: 13px; letter-spacing: 1px; color: var(--rule);
  }
  .brand-tagline::before, .brand-tagline::after {
    content: ""; width: 46px; height: 1.5px; background: var(--rule);
  }
  .letter-body {
    position: absolute; left: 86px; top: 198px; width: 744px;
    font-size: 14.5px; line-height: 26.5px; color: var(--ink-soft);
  }
  .issue-date { margin-bottom: 9px; }
  .recipient { line-height: 18px; margin-bottom: 50px; }
  .salutation { margin-bottom: 26px; }
  .letter-body p.paragraph { margin-bottom: 26.5px; text-align: justify; }
  .closing { margin-top: 52px; }
  .signature-mark {
    display: block; width: 212px; height: 26px; margin: 14px 0 8px;
  }
  .signer-name { font-size: 17px; font-weight: 600; color: var(--ink); line-height: 24px; }
  .signer-title { font-size: 14.5px; line-height: 26px; }
  .footer-art {
    position: absolute; left: 0; top: 938px; width: 270px; height: 166px;
  }
  .footer-band {
    position: absolute; left: 0; top: 1103px; width: 100%; height: 77px;
    background: var(--brand-purple);
    font-family: "Lato", Arial, sans-serif; color: #fff; font-size: 17px;
    display: flex;
  }
  .footer-col {
    display: flex; flex-direction: column; justify-content: center;
    height: 100%;
  }
  .footer-col + .footer-col { border-left: 1px solid rgba(255,255,255,0.55); }
  .col-phone { width: 247px; padding-left: 86px; }
  .col-address { width: 305px; padding-left: 18px; }
  .col-web { padding-left: 22px; }
  .contact-line { display: flex; align-items: center; gap: 7px; line-height: 22px; }
  .contact-line svg { width: 16px; height: 16px; fill: #fff; flex: none; }
  .address-line { display: flex; gap: 8px; line-height: 21px; }
  .address-line svg { width: 15px; height: 20px; fill: #fff; flex: none; margin-top: 1px; }
</style>
</head>
<body>
<main class="letterhead">
  <header class="brand">
    <div class="brand-name">MERIDIAN</div>
    <div class="brand-tagline">Realty Group, LLC</div>
  </header>

  <section class="letter-body">
    <p class="issue-date">Issuing Date: May 5, 2018</p>
    <p class="recipient">Name Of Employee Mr. XYZABC<br>Address of Employee<br>Address Line 2 etc..</p>
    <p class="salutation">Dear Mr.XYZABC</p>
    <p class="paragraph">Lorem Ipsum has been the industry's standard dummy text ever since the 1500s, when an unknown printer took a galley of type and scrambled it to make a type specimen book. It has survived not only five centuries, but also the leap into electronic typesetting, remaining essentially unchanged. It was popularised in the 1960s with the release of Letraset sheets containing Lorem Ipsum passages, and more recently with desktop publishing software like Aldus PageMaker including versions of Lorem Ipsum.</p>
    <p class="paragraph">Lorem Ipsum is simply dummy text of the printing and typesetting industry. Lorem Ipsum has been the industry's standard dummy text ever since the 1500s, when an unknown printer took a galley of type and scrambled it to make a type specimen book.</p>
    <p class="paragraph">It has survived not only five centuries, but also the leap into electronic typesetting, remaining essentially unchanged. It was popularised in the 1960s with the release of Letraset sheets containing Lorem IpsumIpsum passages.</p>
    <p class="closing">Yours Sincerely</p>
    <svg class="signature-mark" role="img" aria-label="Handwritten signature of Daniel Brooks" viewBox="0 0 212 26">
      <rect x="0" y="8" width="212" height="12" rx="6" fill="#e6e6e6"/>
    </svg>
    <p class="signer-name">Daniel Brooks</p>
    <p class="signer-title">Managing Director</p>
  </section>

  <svg class="footer-art" role="img" aria-label="Illustration of an archer drawing a bow, rising from the footer band" viewBox="0 0 270 166" preserveAspectRatio="none">
    <defs>
      <linearGradient id="artFade" x1="0" y1="1" x2="0.6" y2="0">
        <stop offset="0" stop-color="#4f2a87" stop-opacity="0.9"/>
        <stop offset="1" stop-color="#7a59b0" stop-opacity="0.15"/>
      </linearGradient>
    </defs>
    <rect x="0" y="0" width="270" height="166" fill="url(#artFade)"/>
  </svg>

  <footer class="footer-band">
    <div class="footer-col col-phone">
      <div class="contact-line">
        <svg viewBox="0 0 16 16"><path d="M2 5c0-2 3-3 6-3s6 1 6 3v1h-3V5H5v1H2z"/><path d="M4 7h8l2 6H2z"/></svg>
        555.010.4821
      </div>
      <div class="contact-line">
        <svg viewBox="0 0 16 16"><rect x="4" y="1" width="8" height="4"/><rect x="1" y="6" width="14" height="6" rx="1"/><rect x="4" y="10" width="8" height="5"/></svg>
        555.010.4822
      </div>
    </div>
    <div class="footer-col col-address">
      <div class="address-line">
        <svg viewBox="0 0 15 20"><path d="M7.5 0a7 7 0 0 0-7 7c0 5 7 13 7 13s7-8 7-13a7 7 0 0 0-7-7zm0 10a3 3 0 1 1 0-6 3 3 0 0 1 0 6z"/></svg>
        <span>140 Linden Avenue, Northport,<br>NY 11700 | Suite 210</span>
      </div>
    </div>
    <div class="footer-col col-web">
      <div class="contact-line">
        <svg viewBox="0 0 16 16"><path d="M1 3h14v10H1z M2 4l6 5 6-5" fill="none" stroke="#fff" stroke-width="1.6"/></svg>
        dana.reyes@meridianrealty.com
      </div>
      <div class="contact-line">
        <svg viewBox="0 0 16 16"><g fill="none" stroke="#fff" stroke-width="1.4"><circle cx="8" cy="8" r="6.5"/><ellipse cx="8" cy="8" rx="3" ry="6.5"/><path d="M1.5 8h13M3 4.5h10M3 11.5h10"/></g></svg>
        www.meridianrealty.com
      </div>
    </div>
  </footer>
</main>
</body>
</html>
```